Layout of a 14-page report

I need a professional, well-designed, layout for a 14-page free report I'm offering.
My colors are red/black/white and have a chalkboard theme in my header graphic which you can incorporate if you want: see my website here - http://larkavell.example/. I am an SEO strategy consultant and this report is about "Ranking Basics."
The attachment contains a few images/designs and graphics I like that may help guide your creative process.
I would like to see the:
1. Cover page
2. inside spread layout of a standard page
3. inside spread layout of a "page with sidebar content" (indicated in the attachment)
The selected winner will complete all pages. Thank you!

```html
<!DOCTYPE html>
<html lang="en">
<head>
<meta charset="utf-8">
<title>Table of Contents – Ranking Basics</title>
<link rel="stylesheet" href="https://fonts.googleapis.com/css2?family=Anton&family=Delius&display=swap">
<style>
  :root {
    --page-grey: #d4d5d7;
    --page-light: #ffffff;
    --title-red: #e32b3c;
    --dot-red: #c4161c;
    --ink: #1c1c1c;
    --gear-salmon: #e0957a;
    --gear-grey: #b9babc;
    --footer-black: #000000;
  }
  * { box-sizing: border-box; margin: 0; padding: 0; }
  html, body { width: 848px; height: 1200px; overflow: hidden; background: var(--page-light); }
  .page {
    position: relative;
    width: 848px;
    height: 1200px;
    overflow: hidden;
    font-family: "Delius", "Comic Neue", cursive;
    color: var(--ink);
  }
  .page-body {
    position: absolute;
    inset: 0 0 83px 0;
    background: linear-gradient(90deg, var(--page-grey) 0%, #eceded 30%, var(--page-light) 62%, #f2f2f3 80%, var(--page-grey) 100%);
  }
  .gear-artwork {
    position: absolute;
    left: 0; top: 0;
    width: 530px; height: 450px;
    background:
      radial-gradient(circle at 185px 200px, rgba(224,149,122,.85) 0 90px, rgba(224,149,122,.35) 140px, transparent 160px),
      radial-gradient(circle at 378px 100px, rgba(224,149,122,.75) 0 55px, transparent 85px),
      radial-gradient(circle at 80px 360px, rgba(224,149,122,.6) 0 50px, transparent 75px),
      radial-gradient(circle at 375px 265px, rgba(185,186,188,.7) 0 50px, transparent 75px),
      radial-gradient(circle at 480px 190px, rgba(185,186,188,.5) 0 35px, transparent 55px),
      radial-gradient(circle at 250px 30px, rgba(185,186,188,.55) 0 40px, transparent 65px);
  }
  .title {
    position: absolute;
    right: 98px;
    top: 262px;
    font-family: "Anton", "Oswald", sans-serif;
    font-weight: 400;
    font-size: 74px;
    line-height: 70px;
    letter-spacing: 1px;
    color: var(--title-red);
    text-align: right;
  }
  .intro, .back-matter li {
    position: relative;
    list-style: none;
  }
  .intro {
    position: absolute;
    left: 200px;
    top: 533px;
    font-size: 26px;
  }
  .intro::before, .back-matter li::before {
    content: "";
    position: absolute;
    left: -25px;
    top: 50%;
    width: 10px; height: 10px;
    margin-top: -4px;
    border-radius: 50%;
    background: var(--dot-red);
  }
  .chapters {
    position: absolute;
    left: 128px;
    top: 594px;
    list-style: none;
    font-size: 17.5px;
  }
  .chapters li {
    display: grid;
    grid-template-columns: 38px 34px auto;
    align-items: start;
    line-height: 20px;
    margin-bottom: 9.5px;
  }
  .chapters .check {
    width: 20px; height: 20px;
    border: 1.5px solid var(--dot-red);
    border-radius: 50%;
  }
  .back-matter {
    position: absolute;
    left: 199px;
    top: 880px;
    font-size: 24px;
    line-height: 34px;
  }
  .footer-band {
    position: absolute;
    left: 0; right: 0; bottom: 0;
    height: 28px;
    background: var(--footer-black);
  }
</style>
</head>
<body>
<main class="page">
  <div class="page-body"></div>
  <div class="gear-artwork" role="img" aria-label="Illustration of interlocking salmon and grey gears, the largest labelled SEO"></div>

  <h1 class="title">Table of<br>Contents</h1>

  <p class="intro">Introduction: A Checklist of Ranking Basics</p>

  <ol class="chapters">
    <li><span class="check"></span><span>1.</span><span>Explore Motivations, Determine KPIs, Manage Expectations</span></li>
    <li><span class="check"></span><span>2.</span><span>“Would You Give This Site Your Credit Card?”</span></li>
    <li><span class="check"></span><span>3.</span><span>Website Marketing Fundamentals: Engagement</span></li>
    <li><span class="check"></span><span>4.</span><span>SEO’s Foundational Individual Elements</span></li>
    <li><span class="check"></span><span>5.</span><span>Take a Holistic View: Benchmark Individual Elements and<br>Then the Site as a Whole</span></li>
    <li><span class="check"></span><span>6.</span><span>Getting Lead Gen Results</span></li>
    <li><span class="check"></span><span>7.</span><span>Foundational SEO: Your First Order of Business</span></li>
    <li><span class="check"></span><span>8:</span><span>Integrate Ongoing SEO into Marketing Routine</span></li>
  </ol>

  <ul class="back-matter">
    <li>Summary</li>
    <li>About Lark</li>
    <li>Resource Links</li>
  </ul>

  <div class="footer-band"></div>
</main>
</body>
</html>
```